Brenmoor Group needs a business card

I would like the card to be simple but modern and elegant.
I like black and white.
or black and gold.
we are a private finance lender and also are involved in property and property developments.

please look at the business card photos i provided i would like B.G only one one side and all the other details on the other side use fonts that tie in with my theme.

Industry/Entity Type

Finance

Contact Information for Business Card

Brenmoor Group (B.G) Callum Brenmoor M: 0418396152 E: callumbren@quivomail.com

Font styles to use
Other font styles liked:
• Use fonts that would reflect our business

Colors
000000
ffffff

Requirements
Must have
• one side of details
• other side has either B.G or Brenmoor Group like in the photos provided

```html
<!DOCTYPE html>
<html lang="en">
<head>
<meta charset="UTF-8">
<title>Brenmoor Group – Business Card</title>
<link rel="stylesheet" href="https://fonts.googleapis.com/css2?family=Montserrat:wght@400;600&display=swap">
<style>
  :root {
    --backdrop: #1c1c1e;
    --card-black: #0b0b0c;
    --card-edge: #161617;
    --ink-white: #f2f2f2;
    --ink-soft: #c9c9c9;
    --gloss-black: #2c2c2e;
  }
  * { margin: 0; padding: 0; box-sizing: border-box; }
  html, body {
    width: 1200px;
    height: 786px;
    overflow: hidden;
    background: var(--backdrop);
  }
  .canvas {
    width: 1200px;
    height: 786px;
    display: flex;
    align-items: center;
    justify-content: center;
    gap: 60px;
    font-family: "Montserrat", Arial, sans-serif;
  }
  .card {
    width: 520px;
    height: 297px;
    background: var(--card-black);
    border: 1px solid var(--card-edge);
    border-radius: 3px;
    position: relative;
    box-shadow: 0 18px 40px rgba(0, 0, 0, 0.45);
  }
  .card--details {
    display: flex;
    align-items: center;
    justify-content: center;
  }
  .details {
    display: flex;
    flex-direction: column;
    align-items: center;
    margin-left: 70px;
  }
  .details__name {
    color: var(--ink-white);
    font-weight: 600;
    font-size: 17px;
    letter-spacing: 1.5px;
    text-transform: uppercase;
  }
  .details__rule {
    width: 190px;
    height: 1px;
    background: var(--ink-soft);
    margin: 10px 0 12px;
  }
  .details__line {
    color: var(--ink-soft);
    font-weight: 400;
    font-size: 12px;
    letter-spacing: 0.6px;
    line-height: 1.7;
  }
  .card--brand {
    display: flex;
    align-items: center;
    justify-content: center;
  }
  .brand-name {
    color: var(--gloss-black);
    font-weight: 400;
    font-size: 34px;
    letter-spacing: 0.5px;
    margin-top: 40px;
  }
</style>
</head>
<body>
  <main class="canvas">
    <section class="card card--details" aria-label="Card back with contact details">
      <div class="details">
        <h1 class="details__name">Callum Brenmoor</h1>
        <div class="details__rule"></div>
        <p class="details__line">M: 0418396152</p>
        <p class="details__line">E: callumbren@quivomail.com</p>
      </div>
    </section>
    <section class="card card--brand" aria-label="Card front with company name">
      <p class="brand-name">Brenmoor Group</p>
    </section>
  </main>
</body>
</html>
```